Flyer-Design für Dienstleistungen im vorbeugenden Brandschutz und der Ersten Hilfe
Zielgruppe
Wachturm Brandschutz & Erste-Hilfe
Meine Firma spezialisiert sich auf Dienstleistungen im vorbeugenden Brandschutz und im Bereich der Ersten Hilfe.
Mit meiner Firma biete ich folgende Dienstleistungen und Produkte an:
Diensteistungen:
- jährliche Brandschutzunterweisung
- Brandschutzhelferausbildungen nach DGUV Information 205-023
- Brandsicherheitswachen für Unternehmen und Veranstaltungen
- Sanitätsdienste für Unternehmen und Veranstaltungen
- externer Brandschutzbeauftragter
- Vertrieb und Wartung von Feuerlöschern / Brandschutzbedarf
- betriebliche Erste-Hilfe Schulungen / Erste Hilfe Kurs für den Führerschein
- Wartung und Vertrieb von Erste-Hilfe-Material / Ausstattung
- Wartung, Vertrieb und Schulungen von Automatisierten Externen Defibrillatoren
Zu den folgenden Dienstleistungen sollte die Möglichkeit bestehen, detaillierte Texte einzusetzen. Die Themengebite können auch zusammengefasst werden:
Themengebiet 1 (Brandschutz)
Themengebiet 2 (Erste-Hilfe)
Meine Zielgruppe sind primär Firmen, allerdings biete ich die Dienstleistungen auch an Privatpersonen an.
Aufgabenstellung
Die Schriftart in meinem Logo ist 'Avenir'.
Die Firmenfarben orange und grau sollten berücksichtigt werden.
Das Format sollte DIN A4 doppelseitig bedruckt und in 3 Teile gefaltet sein (Ergebnis DIN Lang)
Auf der letzten Seite sollten die Kontaktdaten stehen, sowie mindestens das Logo (Mitglied im BKSV (Bund Kommunaler Sicherheits-Vereine))

```html
<!DOCTYPE html>
<html lang="de">
<head>
<meta charset="utf-8">
<title>Wachturm Sanitätsdienst – Flyer</title>
<link href="https://fonts.googleapis.com/css2?family=Nunito+Sans:ital,wght@0,300;0,400;0,600;1,400;1,600&display=swap" rel="stylesheet">
<style>
  :root{
    --orange:#e8521c;
    --orange-cross:#ee6f1e;
    --grey-text:#5a5a5f;
    --grey-dark:#3d3d42;
    --paper:#ededee;
    --band:#c4c2c4;
    --stage:#e9e6df;
  }
  *{box-sizing:border-box;margin:0;padding:0}
  html,body{width:800px;height:1200px;overflow:hidden}
  body{background:var(--stage);font-family:"Nunito Sans",sans-serif;position:relative}
  .flyer{position:absolute;left:40px;top:90px;width:720px;display:flex;flex-direction:column;box-shadow:0 10px 30px rgba(0,0,0,.15)}
  .panel{position:relative;width:720px;height:340px;overflow:hidden}
  .panel--cover{background:var(--paper)}
  .panel--fire{background:var(--band)}
  .panel--aid{background:var(--paper)}

  .brand{position:absolute;left:50px;top:38px;display:flex;align-items:center;gap:12px}
  .brand__dot{width:14px;height:14px;border-radius:50%;background:var(--orange)}
  .brand__name{font-size:40px;font-weight:300;line-height:1;color:var(--orange);letter-spacing:.3px}
  .tagline{position:absolute;left:50px;top:108px;width:420px;font-size:18px;font-weight:300;color:var(--grey-text);line-height:1.35;letter-spacing:.4px}
  .intro{position:absolute;left:50px;top:180px;width:400px;font-size:16px;font-weight:300;color:var(--grey-text);line-height:1.45;letter-spacing:.3px}
  .cover-photo{position:absolute;right:30px;top:110px;width:210px;height:200px;border:2px solid var(--orange);border-radius:16px;
    background:linear-gradient(135deg,#dcd8d5 0%,#b02530 55%,#6e1016 100%)}

  .section-title{font-size:20px;font-weight:400;letter-spacing:3px;color:var(--orange);text-transform:uppercase;margin-bottom:12px}
  .service-list{list-style:none}
  .service-list li{position:relative;padding-left:16px;margin-bottom:4px}
  .service-list li::before{content:"";position:absolute;left:0;top:.6em;width:6px;height:6px;border:1px solid currentColor;border-radius:50%}

  .fire-copy{position:absolute;left:60px;top:50px;width:480px}
  .fire-copy .service-list{font-size:16px;font-style:italic;font-weight:600;color:var(--grey-dark);line-height:1.4}

  .aid-photo{position:absolute;left:40px;top:35px;width:270px;height:270px;border:2px solid var(--orange);border-radius:16px;
    background:linear-gradient(135deg,#c23a3a 0%,#d8d4d2 50%,#7a8aa6 100%)}
  .aid-cross{position:absolute;left:130px;top:110px;width:130px;height:130px}
  .aid-copy{position:absolute;left:350px;top:50px;width:340px}
  .aid-copy .service-list{font-size:16px;font-weight:300;color:var(--grey-text);line-height:1.4;letter-spacing:.3px}
</style>
</head>
<body>
  <main class="flyer">
    <section class="panel panel--cover">
      <div class="brand">
        <span class="brand__dot"></span>
        <span class="brand__name">Wachturm Sanitätsdienst</span>
      </div>
      <p class="tagline">Dienstleistungen im vorbeugenden Brandschutz und im Bereich der Ersten Hilfe</p>
      <p class="intro">Wir setzten dabei auf die hohe Kompetenz und Erfahrung unserer Mitarbeiter, die alle aus der Feuerwehr oder aus dem Rettungsdienst kommen.</p>
      <div class="cover-photo" role="img" aria-label="Foto: Prüfung eines roten Feuerlöschers am Manometer"></div>
    </section>

    <section class="panel panel--fire">
      <div class="fire-copy">
        <h2 class="section-title">Brandschutz</h2>
        <ul class="service-list">
          <li>jährliche Brandschutzunterweisung</li>
          <li>Brandschutzhelferausbildungen nach DGUV Information 205-023</li>
          <li>Vertrieb und Wartung von Feuerlöschern / Brandschutzbedarf</li>
        </ul>
      </div>
    </section>

    <section class="panel panel--aid">
      <div class="aid-photo" role="img" aria-label="Foto: Erste-Hilfe-Schulung mit Übungspuppe und Teilnehmenden"></div>
      <svg class="aid-cross" viewBox="0 0 130 130" aria-hidden="true">
        <path d="M40 0 H90 V40 H130 V90 H90 V130 H40 V90 H0 V40 H40 Z" fill="var(--orange-cross)"/>
      </svg>
      <div class="aid-copy">
        <h2 class="section-title">Erste Hilfe</h2>
        <ul class="service-list">
          <li>betriebliche Erste-Hilfe Schulungen / Erste Hilfe Kurs für den Führerschein</li>
          <li>Wartung und Vertrieb von Erste-Hilfe-Material / Ausstattung</li>
          <li>Wartung, Vertrieb und Schulungen von Automatisierten Externen Defibrillatoren</li>
        </ul>
      </div>
    </section>
  </main>
</body>
</html>
```